Brindle Yard Care. The best in the biz

I run a lawn care service that offers full service mowing. 100% satisfaction guarantee. Fast, Friendly, quality service "I am your lawns best friend" I cut residential lawns. I offer a mow package that includes trimming, edging and clean up. Prices very from 20 dollars to 75. I want my logo to stand out. Free estimates

Target Market(s)

Home owners

Industry/Entity Type

Landscaping

Contact Information for Business Card

482-615-0273 tomkerl47@quillmail.net Dorian. Brindle Yard care

Colors
f37122
9bcb3c
cadf82

Requirements
Must have
• Company name.
• Phone number
• Email
• My services
• images
Nice to have
• A sun that is growing grass.
Should not have
• Incorrect information

```html
<!DOCTYPE html>
<html lang="en">
<head>
<meta charset="utf-8">
<title>Brindle Yard Care – Business Card</title>
<link href="https://fonts.googleapis.com/css2?family=Open+Sans:wght@400;600;700&display=swap" rel="stylesheet">
<style>
  :root {
    --backdrop: #d9d9d9;
    --card-black: #000000;
    --lawn-green: #9bcb3c;
    --sun-orange: #f37122;
    --soft-green: #cadf82;
    --badge-grey: #5e5f61;
    --white: #ffffff;
    --card-w: 600px;
    --card-h: 343px;
  }
  * { box-sizing: border-box; margin: 0; padding: 0; }
  html, body {
    width: 1200px; height: 900px; overflow: hidden;
    background: var(--backdrop);
    font-family: "Open Sans", Arial, sans-serif;
  }
  .canvas {
    width: 1200px; height: 900px;
    display: flex; flex-direction: column;
    align-items: center; justify-content: center; gap: 50px;
  }
  .card {
    position: relative;
    width: var(--card-w); height: var(--card-h);
    background: var(--card-black);
    overflow: hidden;
    box-shadow: 0 2px 6px rgba(0,0,0,.18);
  }

  /* Back side */
  .card-back { text-align: center; color: var(--lawn-green); }
  .card-back .badge {
    display: block; margin: 34px auto 0;
    width: 70px; height: 70px; border-radius: 50%;
    background: var(--badge-grey);
    border: 5px solid var(--lawn-green);
  }
  .card-back .company-name {
    font-size: 38px; font-weight: 400; letter-spacing: .5px;
    margin-top: 8px; line-height: 1.15;
  }
  .card-back .taglines {
    list-style: none; margin-top: 14px;
    font-size: 17px; font-weight: 600; line-height: 1.55;
  }

  /* Front side */
  .card-front .swoosh { position: absolute; inset: 0; width: 100%; height: 100%; }
  .card-front .badge {
    position: absolute; left: 62px; top: 68px;
    width: 206px; height: 206px; border-radius: 50%;
    background: var(--badge-grey);
    border: 8px solid var(--lawn-green);
    display: flex; align-items: center; justify-content: center;
    text-align: center;
  }
  .card-front .badge-name {
    color: var(--lawn-green);
    font-size: 24px; font-weight: 600; line-height: 1.2;
  }
  .card-front .contact {
    position: absolute; right: 34px; top: 170px;
    text-align: right; color: var(--white);
  }
  .contact .person { font-size: 20px; font-weight: 700; margin-bottom: 12px; }
  .contact .line {
    display: flex; align-items: center; justify-content: flex-end; gap: 8px;
    font-size: 17px; line-height: 1.35;
  }
  .contact .line svg { width: 14px; height: 14px; flex: none; }
</style>
</head>
<body>
<main class="canvas">

  <section class="card card-back" aria-label="Card back">
    <span class="badge" aria-hidden="true"></span>
    <h1 class="company-name">Brindle Yard Care</h1>
    <ul class="taglines">
      <li>100% satisfaction guarantee.</li>
      <li>Fast, Friendly, Quality Service</li>
      <li>I am your lawns best friend</li>
    </ul>
  </section>

  <section class="card card-front" aria-label="Card front">
    <svg class="swoosh" viewBox="0 0 600 343" preserveAspectRatio="none" aria-hidden="true">
      <path d="M372 0 C470 70 450 250 250 343 L292 343 C478 255 498 80 402 0 Z" fill="var(--sun-orange)"/>
      <path d="M402 0 C498 80 478 255 292 343 L600 343 L600 0 Z" fill="var(--lawn-green)"/>
      <path d="M372 0 C470 70 450 250 250 343" fill="none" stroke="#000" stroke-width="3"/>
      <path d="M402 0 C498 80 478 255 292 343" fill="none" stroke="#000" stroke-width="3"/>
    </svg>

    <div class="badge">
      <span class="badge-name">Brindle<br>Yard Care</span>
    </div>

    <address class="contact" style="font-style:normal">
      <p class="person">Dorian</p>
      <p class="line">482-615-0273
        <svg viewBox="0 0 24 24" aria-hidden="true"><path fill="#fff" d="M6.6 10.8a15.1 15.1 0 0 0 6.6 6.6l2.2-2.2a1 1 0 0 1 1-.25 11.4 11.4 0 0 0 3.6.57 1 1 0 0 1 1 1V20a1 1 0 0 1-1 1A17 17 0 0 1 3 4a1 1 0 0 1 1-1h3.5a1 1 0 0 1 1 1c0 1.25.2 2.45.57 3.57a1 1 0 0 1-.25 1z"/></svg>
      </p>
      <p class="line">tomkerl47@quillmail.net
        <svg viewBox="0 0 24 24" aria-hidden="true"><path fill="#fff" d="M3 5h18v14H3z"/><path d="M3 5l9 7 9-7" fill="none" stroke="var(--lawn-green)" stroke-width="2"/></svg>
      </p>
    </address>
  </section>

</main>
</body>
</html>
```